Horizzontal format 2 m long x 0,80 m high

We need a horizzontal format design for a rectangular board 2m long and 0,8 meter high.

The board will be positioned on a side of soccer fields, so the text should be readable for the other side of the field.
Color:text colors should be read, and grey.

Copy:
"Murovanti Impresa Edile.
Pensiamo a TUTTO NOI, dall'ideazione alla REALIZZAZIONE

Ristrutturazioni d'Interni ed Esterni,
Progettazione con la collaborazione di un TEAM DI ARCHITETTI E INGEGNERI
Realizzazione con materiali di altissimo livello (only if there is enough space!)
CURA DEI particolari per ottenere grandi risultati (only if there is enough space!)

TOTAL RELAX con Murovanti Impresa Edile"

CTA: Richiedi subito una consulenza gratui
Riferimenti:
3421857630
info@murovanti-esempio.it
murovanti-esempio.it
seguici su Facebook

Target Market(s)

Man & Woman 26+, medium income, house owners, soccer fans. The board will be showed during soccer games,

Industry/Entity Type

Construction Company

Colors
ec1f27
eaf1f7
f3f1f8
cedeed

Requirements
Must have
• Murovanti Logo.
• Charater text very big, it must be readable from the other side of a soccer filed.
• Text and services are the center of the requested design. Images are not necessary.
Nice to have
• It would be nice if play with differt background colors (almost grey and red, but you could use also other colors, like light grey for example!). We'd like not only "rectangular lines" to divide the spaces.

```html
<!DOCTYPE html>
<html lang="it">
<head>
<meta charset="utf-8">
<title>Murovanti Impresa Edile – Cartellone bordo campo</title>
<link rel="stylesheet" href="https://fonts.googleapis.com/css2?family=Anton&family=Roboto+Condensed:wght@700&display=swap">
<style>
  :root {
    --red: #ec1f27;
    --deep-red: #d8141c;
    --ink: #1f1f1f;
    --band-dark: #222222;
    --white: #ffffff;
    --page: #e6ebf0;
    --photo-light: #eaf1f7;
    --photo-mid: #cedeed;
    --photo-warm: #c9a86a;
    --logo-grey: #b9bcc2;
  }
  html, body {
    margin: 0;
    width: 1200px;
    height: 927px;
    overflow: hidden;
    background: var(--page);
  }
  .board {
    position: absolute;
    left: 20px;
    top: 231px;
    width: 1160px;
    height: 464px;
    box-shadow: 0 6px 24px rgba(0,0,0,.18);
  }
  .board svg { display: block; }
  .headline { font-family: "Anton", sans-serif; }
  .service { font-family: "Roboto Condensed", sans-serif; font-weight: 700; }
  .brand-name { font-family: "Anton", sans-serif; fill: var(--red); }
</style>
</head>
<body>
<div class="board">
<svg width="1160" height="464" viewBox="0 0 1160 464" xmlns="http://www.w3.org/2000/svg">
  <defs>
    <linearGradient id="interior" x1="0" y1="0" x2="1" y2="1">
      <stop offset="0" stop-color="var(--photo-light)"/>
      <stop offset="1" stop-color="var(--photo-mid)"/>
    </linearGradient>
    <linearGradient id="room-warm" x1="0" y1="0" x2="1" y2="1">
      <stop offset="0" stop-color="var(--photo-warm)"/>
      <stop offset="1" stop-color="#4a3f35"/>
    </linearGradient>
    <linearGradient id="room-cool" x1="0" y1="0" x2="1" y2="1">
      <stop offset="0" stop-color="#d7dbe0"/>
      <stop offset="1" stop-color="#5b6068"/>
    </linearGradient>
  </defs>

  <!-- base -->
  <rect class="board-base" width="1160" height="464" fill="var(--white)"/>

  <!-- logo area -->
  <g class="logo">
    <rect x="70" y="58" width="22" height="22" fill="var(--red)"/>
    <text class="brand-name" x="102" y="80" font-size="32" letter-spacing="1">MUROVANTI</text>
  </g>

  <!-- interior image area -->
  <rect class="interior-photo" x="0" y="141" width="440" height="323" fill="url(#interior)" role="img" aria-label="Foto di un ufficio moderno con pareti in vetro e parete decorativa bianca"/>

  <!-- red header band -->
  <path class="band-header" d="M441 0 H1160 V141 H405 Q420 70 441 0 Z" fill="var(--red)"/>
  <!-- dark slogan band -->
  <path class="band-slogan" d="M408 298 H1160 V356 H410 Z" fill="var(--band-dark)"/>
  <!-- red contact band -->
  <path class="band-contact" d="M410 356 H1160 V464 H440 Q420 410 410 356 Z" fill="var(--red)"/>

  <!-- round image frames -->
  <circle cx="381" cy="95" r="58" fill="url(#room-warm)" stroke="var(--white)" stroke-width="4" role="img" aria-label="Foto di un ufficio con parete gialla"/>
  <circle cx="371" cy="232" r="58" fill="url(#room-cool)" stroke="var(--white)" stroke-width="4" role="img" aria-label="Foto di un soggiorno moderno con vetrate"/>
  <circle cx="386" cy="385" r="58" fill="url(#room-warm)" stroke="var(--white)" stroke-width="4" role="img" aria-label="Foto di un salotto luminoso con divano bianco"/>

  <!-- headline -->
  <text class="headline" x="457" y="85" font-size="64" fill="var(--white)" textLength="682" lengthAdjust="spacingAndGlyphs">Murovanti Impresa Edile.</text>
  <text class="headline" x="457" y="127" font-size="27" fill="#2a0b0b" textLength="682" lengthAdjust="spacingAndGlyphs">Pensiamo a TUTTO NOI, dall'ideazione alla REALIZZAZIONE</text>

  <!-- services -->
  <text class="service" x="457" y="186" font-size="38" fill="var(--red)" textLength="682" lengthAdjust="spacingAndGlyphs">Ristrutturazioni d'Interni ed Esterni,</text>
  <text class="service" x="457" y="228" font-size="38" fill="var(--red)" textLength="682" lengthAdjust="spacingAndGlyphs">Progettazione con la collaborazione di un</text>
  <text class="headline" x="457" y="284" font-size="54" fill="var(--red)" textLength="682" lengthAdjust="spacingAndGlyphs">TEAM DI ARCHITETTI E INGEGNERI</text>

  <!-- slogan -->
  <text class="headline" x="457" y="347" font-size="42" fill="var(--deep-red)" textLength="682" lengthAdjust="spacingAndGlyphs">TOTAL RELAX con Murovanti Impresa Edile”</text>

  <!-- call to action -->
  <text class="headline" x="457" y="402" font-size="38" fill="var(--white)" textLength="682" lengthAdjust="spacingAndGlyphs">CTA: Richiedi subito una consulenza gratui</text>

  <!-- contacts -->
  <g class="contacts service" fill="var(--white)">
    <text x="457" y="432" font-size="23" textLength="120" lengthAdjust="spacingAndGlyphs">Riferimenti:</text>
    <circle cx="592" cy="425" r="6" fill="var(--white)"/>
    <text x="602" y="432" font-size="19" textLength="98" lengthAdjust="spacingAndGlyphs">3421857630</text>
    <rect x="706" y="420" width="12" height="9" fill="none" stroke="var(--white)" stroke-width="1.5"/>
    <path d="M706 420 L712 425 L718 420" fill="none" stroke="var(--white)" stroke-width="1.2"/>
    <text x="722" y="432" font-size="19" textLength="184" lengthAdjust="spacingAndGlyphs">info@murovanti-esempio.it</text>
    <circle cx="917" cy="425" r="6" fill="none" stroke="var(--white)" stroke-width="1.5"/>
    <text x="927" y="432" font-size="19" textLength="133" lengthAdjust="spacingAndGlyphs">murovanti-esempio.it</text>
    <circle cx="1071" cy="425" r="6" fill="var(--white)"/>
    <text x="1081" y="432" font-size="21" textLength="58" lengthAdjust="spacingAndGlyphs">seguici su</text>
  </g>
</svg>
</div>
</body>
</html>
```